This book will apply the 12 Steps to gaming addiction, also known as video game addiction. The primary purpose of the book is to provide an effective solution for this new type of addiction. The solution is based on the rich and successful concepts of traditional twelve-step programs like RL.

The title on the cover will be "Nine Doors Past the Glowing Screen" and "by Martin Quorby". A subtitle can be used if it works in your design of "A Practical Path Beyond Compulsive Console Play". Cover will be for a 6" x 9" book approximately 110 pages in length.

Some back cover text including some review quotes and an author bio are in the attached Word doc. There is also an author photo attached for for the back cover.

Requirements
Must have
• For the cover design it could be stylized, or an image, a partial image, or whatever. I am open to suggestions. Think about what would be noticed by a person searching for help with moderating their video game use, or by the parents or loved ones of problem gamers. Something contemporary and eye catching.

```html
<!DOCTYPE html>
<html lang="en">
<head>
<meta charset="UTF-8">
<title>Nine Doors Past the Glowing Screen — Book Cover</title>
<link rel="stylesheet" href="https://fonts.googleapis.com/css2?family=Cinzel:wght@400;500&display=swap">
<style>
  :root {
    --paper-light: #cfcfcf;
    --paper-mid: #a9a9a9;
    --paper-dark: #6f6f6f;
    --ink: #121212;
    --art-violet: #5b4a8f;
    --art-blue: #3d5fa8;
    --art-deep: #1d2350;
    --art-glow: #8a7fc4;
    --author-ink: #e2e2ea;
  }
  html, body {
    margin: 0;
    padding: 0;
    width: 800px;
    height: 1200px;
    overflow: hidden;
    background: var(--paper-dark);
  }
  .cover {
    position: relative;
    width: 800px;
    height: 1200px;
    overflow: hidden;
    background:
      radial-gradient(ellipse 70% 55% at 50% 42%, var(--paper-light) 0%, var(--paper-mid) 55%, var(--paper-dark) 100%);
  }
  .cover-title {
    position: absolute;
    top: 40px;
    left: 0;
    width: 800px;
    margin: 0;
    text-align: center;
    font-family: "Cinzel", "Times New Roman", serif;
    font-weight: 400;
    font-size: 74px;
    line-height: 106px;
    letter-spacing: 1px;
    text-transform: uppercase;
    color: var(--ink);
  }
  .cover-title span { display: block; }
  .cover-art {
    position: absolute;
    left: 150px;
    top: 450px;
    width: 600px;
    height: 750px;
    border-radius: 48% 52% 0 0 / 38% 40% 0 0;
    background:
      radial-gradient(ellipse 45% 28% at 50% 22%, var(--art-glow) 0%, rgba(91,74,143,0.6) 55%, rgba(91,74,143,0) 100%),
      radial-gradient(ellipse 55% 45% at 50% 72%, var(--art-blue) 0%, var(--art-violet) 50%, rgba(29,35,80,0) 100%),
      linear-gradient(180deg, rgba(91,74,143,0.5) 0%, var(--art-deep) 100%);
    opacity: 0.95;
  }
  .cover-author {
    position: absolute;
    left: 0;
    top: 1140px;
    width: 800px;
    margin: 0;
    text-align: center;
    font-family: "Cinzel", "Times New Roman", serif;
    font-weight: 400;
    font-size: 30px;
    letter-spacing: 1px;
    text-transform: uppercase;
    color: var(--author-ink);
  }
</style>
</head>
<body>
  <main class="cover">
    <h1 class="cover-title">
      <span>Nine Doors Past</span>
      <span>the Glowing</span>
      <span>Screen</span>
    </h1>
    <div class="cover-art" role="img" aria-label="Illustration of a young gamer wearing a headset, with violent video game characters and vehicles bursting out of the top of his head, in purple and blue tones"></div>
    <p class="cover-author">Martin Quorby</p>
  </main>
</body>
</html>
```